Design Executive Business Acquisitons Brokerage Website

Modern but Professional with the colours black, purple and white. Must convey authenticity, and progressive out-of-square thinking. We are a boutique Business Broking firm located in Brisbane QLD Australia. We market and sell businesses with sales revenue/turnover from Au $1M to $15 M + or have a minimum staff of 15 to 50 staff. Our buyers are generally acquisitions corporate buyers. We need a modern approach but conservative tones. We are serious and experienced. We say it as it is and we get the job done! We sell in the following industries but not limited to, engineering, manufacturing, agriculture, recruitment, transportation, warehousing, services, IT,eCommerce, civil construction,mining, wholesaling, dealerships, MEdical (all), service stations, Management rights, high-end retail, building construction,importing,exporting to name a few.

Target Market(s)

SME Corporate Public & Private exsisting large businesses that are looking to buy through acquisitions

Industry/Entity Type

Coommercial executive Business Sale

Number of Pages Required

5+ page

Font styles to use
Sans Serif

Requirements
Must have
• Serious tones, searchar, NDA form, serious corporate executive feel. Include all corporaate colors,black less whit purples.Corporate Logo
Nice to have
• carosel moving right to left of industry pictures as per above and attached industries
Should not have
• No hand shaking, business people.

```html
<!DOCTYPE html>
<html lang="en">
<head>
<meta charset="utf-8">
<title>Corvell Acquisitions Group</title>
<link rel="stylesheet" href="https://fonts.googleapis.com/css2?family=Montserrat:wght@600;700&family=Roboto:wght@400;500;700&display=swap">
<style>
:root{
  --purple:#5b2a7e;
  --purple-dark:#4a1f6a;
  --purple-soft:#6b3a90;
  --ink:#333333;
  --text:#777777;
  --light:#f2f1f4;
  --white:#ffffff;
  --footer:#3b3838;
  --footer-line:#555050;
}
*{margin:0;padding:0;box-sizing:border-box}
html,body{width:1200px;height:4206px;overflow:hidden;background:var(--white)}
body{font-family:'Roboto',sans-serif;color:var(--ink)}
.page{position:relative;width:1200px;height:4206px;overflow:hidden}
.abs{position:absolute}
.heading{font-family:'Montserrat',sans-serif;font-weight:600;text-transform:uppercase;letter-spacing:.5px}
.rule{position:absolute;height:3px;background:var(--purple)}
.rule-wide{position:absolute;height:1px;background:#bbb}
.btn{position:absolute;display:flex;align-items:center;justify-content:center;background:var(--purple);color:var(--white);font-weight:700;font-size:15px;border-radius:26px;text-transform:uppercase}

/* header */
.topbar{position:absolute;left:588px;top:0;width:612px;height:42px;background:var(--purple-dark);display:flex;align-items:center;justify-content:flex-end;gap:60px;padding-right:110px;color:#fff;font-size:15px;font-weight:500}
.topbar .slant{position:absolute;left:0;top:0;width:0;height:0;border-top:42px solid var(--white);border-right:24px solid transparent}
.topbar span{display:flex;align-items:center;gap:10px}
.brand{position:absolute;left:112px;top:30px;display:flex;align-items:center;gap:12px}
.brand .dot{width:46px;height:46px;border-radius:50%;background:var(--purple)}
.brand .name{font-family:'Montserrat',sans-serif;font-weight:700;color:var(--purple);font-size:17px;line-height:20px;text-transform:uppercase;letter-spacing:1px}
.nav{position:absolute;left:450px;top:68px;display:flex;gap:34px;font-size:14px;font-weight:500;color:#333}
.nav .active{color:var(--purple);border-bottom:2px solid var(--purple);padding-bottom:3px}

/* hero */
.hero-photo{position:absolute;left:0;top:116px;width:1200px;height:700px;
  background:
    radial-gradient(ellipse 260px 300px at 520px 250px,rgba(190,160,140,.55),transparent 70%),
    radial-gradient(ellipse 380px 200px at 1000px 330px,rgba(225,228,232,.75),transparent 70%),
    radial-gradient(ellipse 300px 160px at 820px 90px,rgba(70,110,150,.55),transparent 70%),
    linear-gradient(180deg,transparent 55%,rgba(150,110,75,.75) 80%,rgba(120,85,55,.9) 100%),
    linear-gradient(110deg,#3c3d3e 0%,#4b4c4e 30%,#2e3034 55%,#5a5d62 75%,#8d9096 100%)}
.hero-shade{position:absolute;left:600px;top:116px;width:600px;height:520px;background:linear-gradient(90deg,rgba(20,20,25,0),rgba(20,20,25,.35) 30%,rgba(20,20,25,.2))}
.hero-title{left:637px;top:288px;font-size:48px;line-height:54px;color:#fff;font-weight:700}
.hero-copy{left:637px;top:460px;width:440px;font-size:18px;line-height:26px;color:#fff;font-weight:500}
.dots{left:1145px;top:352px;display:flex;flex-direction:column;gap:16px}
.dots i{display:block;width:7px;height:7px;border-radius:50%;background:#fff}

/* about */
.about-bg{position:absolute;left:0;top:770px;width:1200px;height:566px;
  background:
    radial-gradient(ellipse 260px 220px at 180px 170px,rgba(190,175,165,.35),transparent 70%),
    radial-gradient(ellipse 300px 260px at 1000px 300px,rgba(200,185,175,.35),transparent 70%),
    linear-gradient(90deg,#ecebee,#f6f5f7 50%,#efeef1)}
.about-photo{left:130px;top:885px;width:360px;height:360px;border-radius:50%;
  background:
    radial-gradient(ellipse 70px 90px at 250px 150px,#e9c8ae,transparent 75%),
    radial-gradient(ellipse 90px 110px at 270px 130px,#9c5a30,transparent 75%),
    radial-gradient(ellipse 120px 90px at 100px 260px,#3a3c44,transparent 75%),
    linear-gradient(150deg,#f3f2f0 0%,#d8d6d3 40%,#8e8a88 75%,#5d5b5e 100%)}
.about-copy{left:600px;width:488px;font-size:14px;line-height:26px;color:var(--text);text-align:justify}

/* services */
.service{position:absolute;width:310px;text-align:center}
.service .photo{position:relative;margin:0 auto;width:310px;height:290px;border-radius:155px 155px 0 0;border-top:7px solid var(--purple);overflow:hidden}
.service .photo:after{content:"";position:absolute;left:-10%;bottom:-120px;width:120%;height:150px;background:#fff;border-radius:50%}
.s1{background:radial-gradient(ellipse 90px 120px at 110px 140px,#4f86c4,transparent 75%),radial-gradient(ellipse 90px 140px at 260px 120px,#d88a3c,transparent 70%),linear-gradient(140deg,#1d2a3e,#2f4f78 50%,#6b4a2c)}
.s2{background:radial-gradient(ellipse 80px 110px at 180px 150px,#caa27a,transparent 75%),radial-gradient(ellipse 70px 90px at 70px 170px,#8cb46a,transparent 75%),linear-gradient(140deg,#f2f3f2,#dfe2e2 50%,#9a9da2)}
.s3{background:radial-gradient(ellipse 90px 120px at 120px 150px,#c69a80,transparent 75%),radial-gradient(ellipse 100px 130px at 220px 170px,#8f9bb0,transparent 75%),linear-gradient(140deg,#eef0f2,#c9ccd2 55%,#6f7580)}
.service h3{font-size:17px;font-weight:700;margin-top:-14px;position:relative}
.service p{font-size:13px;line-height:24px;color:#999;margin:20px 18px 0}

/* why */
.why{position:absolute;left:0;top:2099px;width:1200px;height:641px;
  background:
    radial-gradient(ellipse 260px 300px at 200px 330px,rgba(130,90,160,.55),transparent 70%),
    radial-gradient(ellipse 300px 320px at 1000px 260px,rgba(120,80,150,.5),transparent 70%),
    linear-gradient(100deg,#55267a,#6c3b92 50%,#58287b)}
.card{position:absolute;width:477px;height:193px;border:2px solid rgba(255,255,255,.85);color:#fff;padding:28px 22px 0 100px}
.card.white{background:#fff;color:#444}
.card h4{font-size:17px;line-height:26px;font-weight:700;text-transform:uppercase}
.card p{font-size:13px;line-height:24px;margin-top:12px;text-align:justify;opacity:.95}
.card.white p{color:#999}
.card svg{position:absolute;left:32px;top:28px}

/* ready */
.ready-photo{position:absolute;left:0;top:2740px;width:1200px;height:472px;
  background:
    radial-gradient(ellipse 110px 140px at 770px 130px,#5a3a2a,transparent 75%),
    radial-gradient(ellipse 200px 220px at 790px 360px,#7d93b0,transparent 75%),
    radial-gradient(ellipse 140px 70px at 650px 440px,#f0eeea,transparent 75%),
    radial-gradient(ellipse 90px 110px at 1150px 290px,#7c9a5c,transparent 75%),
    radial-gradient(ellipse 110px 160px at 1040px 200px,#c9b49a,transparent 75%),
    linear-gradient(90deg,#e4e3e1 0%,#dcdbd9 45%,#cfcac3 70%,#e6e1d9 100%)}
.ready-ring{left:114px;top:2797px;width:360px;height:360px;border-radius:50%;background:#fff;border:10px solid #e4e4e6;text-align:center;padding-top:60px}

/* stories */
.story{position:absolute;width:310px}
.story .photo{height:206px}
.p1{background:radial-gradient(ellipse 70px 90px at 170px 70px,#4a2e24,transparent 75%),radial-gradient(ellipse 120px 70px at 130px 160px,#f4f3f1,transparent 75%),linear-gradient(140deg,#e9e8e6,#c9c5c0 55%,#8c8783)}
.p2{background:radial-gradient(ellipse 90px 80px at 140px 120px,#5e7a92,transparent 75%),radial-gradient(ellipse 80px 90px at 230px 110px,#b8a48a,transparent 75%),linear-gradient(140deg,#f1f2f2,#d8d9da 55%,#9ea2a6)}
.p3{background:radial-gradient(ellipse 100px 110px at 90px 140px,#2c3550,transparent 75%),radial-gradient(ellipse 90px 120px at 250px 130px,#1f2a44,transparent 75%),linear-gradient(140deg,#eef0f2,#c5cbd3 55%,#6f7888)}
.story .caption{position:relative;margin:-40px 18px 0;background:#fff;box-shadow:0 3px 10px rgba(0,0,0,.15);height:147px;text-align:center;padding-top:24px}
.story .caption p{font-size:17px;line-height:25px;color:#333}
.story .caption a{display:inline-block;margin-top:10px;font-size:13px;font-weight:700;color:var(--purple);text-decoration:underline}

/* footer */
.footer{position:absolute;left:0;top:3837px;width:1200px;height:369px;background:var(--footer);color:#fff}
.footer h5{position:absolute;font-size:15px;font-weight:700;text-transform:uppercase}
.footer ul{position:absolute;list-style:none;font-size:14px}
.footer li{height:31px;display:flex;align-items:center;gap:14px}
.footer li:before{content:"";width:12px;height:12px;border-radius:50%;border:2px solid #777}
.ci{position:absolute;left:846px;display:flex;align-items:center;gap:26px;font-size:14px;line-height:20px}
.ci .ring{width:52px;height:52px;border-radius:50%;background:#fff;border:4px solid #8a8585;display:flex;align-items:center;justify-content:center}
.social{position:absolute;left:176px;top:4032px;display:flex;gap:6px}
.social i{width:34px;height:34px;border-radius:50%;border:2px solid #fff;display:flex;align-items:center;justify-content:center}
.social i:before{content:"";width:10px;height:10px;border-radius:50%;background:#fff}
.social i:first-child{background:#fff}
.social i:first-child:before{background:var(--footer)}
</style>
</head>
<body>
<div class="page">

  <div class="topbar"><div class="slant"></div>
    <span><svg width="16" height="12" viewBox="0 0 16 12"><rect x="0" y="0" width="16" height="12" rx="1" fill="#fff"/><path d="M0 1 L8 7 L16 1" stroke="#4a1f6a" stroke-width="1.5" fill="none"/></svg>hello@corvellgroup.example</span>
    <span><svg width="14" height="14" viewBox="0 0 24 24"><path fill="#fff" d="M6.6 10.8a15.1 15.1 0 006.6 6.6l2.2-2.2c.3-.3.7-.4 1-.2 1.1.4 2.3.6 3.6.6.6 0 1 .4 1 1V20c0 .6-.4 1-1 1C10.6 21 3 13.4 3 4c0-.6.4-1 1-1h3.5c.6 0 1 .4 1 1 0 1.3.2 2.5.6 3.6.1.3 0 .7-.2 1z"/></svg>+1 (555) 014 2290</span>
  </div>
  <div class="brand"><div class="dot"></div><div class="name">Corvell<br>Acquisitions Group</div></div>
  <nav class="nav"><span class="active">HOME</span><span>ABOUT US</span><span>OUR SERVICES</span><span>WHY CHOOSE US</span><span>EVENTS</span><span>CONTACT US</span></nav>

  <div class="hero-photo" role="img" aria-label="Photo of a smiling businessman at a desk with a computer in an office"></div>
  <div class="hero-shade"></div>
  <div class="about-bg" role="img" aria-label="Faint background photo of a team working in an office"></div>
  <svg class="abs" style="left:0;top:600px" width="1200" height="240" viewBox="0 0 1200 240">
    <path d="M0 37 Q600 370 1200 37 L1200 240 L0 240 Z" fill="#f1f0f3"/>
    <path d="M0 60 Q600 400 1200 60" stroke="#5b2a7e" stroke-width="6" fill="none"/>
    <circle cx="600" cy="180" r="52" fill="#fff" stroke="#e6e3ea" stroke-width="4"/>
    <circle cx="600" cy="180" r="20" fill="#5b2a7e"/>
  </svg>
  <h1 class="abs heading hero-title" style="letter-spacing:0">Corvell<br>Acquisitions<br>Group</h1>
  <p class="abs hero-copy">Lorem ipsum dolor sit amet, consectetur adipisc ing elit sed do eiusmod tempea.</p>
  <div class="btn" style="left:637px;top:536px;width:155px;height:45px;font-size:14px">Get Started</div>
  <div class="abs dots"><i></i><i style="width:14px;height:14px;margin-left:-3px;opacity:.6"></i><i></i><i></i></div>

  <div class="abs about-photo" role="img" aria-label="Circular photo of a woman smiling with colleagues working behind her"></div>
  <h2 class="abs heading" style="left:600px;top:878px;font-size:38px">About Us</h2>
  <div class="rule" style="left:600px;top:928px;width:42px"></div>
  <div class="rule-wide" style="left:642px;top:929px;width:45px"></div>
  <p class="abs about-copy" style="top:966px">Lorem ipsum dolor sit amet, consectetur adipiscing elit, sed do eiusmod tempor incididunt ut labore et dolore magna aliqua. Ut enim ad minim veniam, quis nostrud exercitation ullamco laboris nisi ut aliquip ex ea com modo conseque irure dolor in reprehenderitea.</p>
  <p class="abs about-copy" style="top:1080px">Aincididunt ut labore et dolore magna aliqua. Ut enim ad minim veniam, quis nostrud exercitation ullamco laboris nisi ut aliquip ex ea com modo conseque irure dolor in reprehenderitea.</p>
  <div class="btn" style="left:600px;top:1194px;width:153px;height:48px">Learn More</div>

  <h2 class="abs heading" style="left:0;width:1200px;text-align:center;top:1433px;font-size:38px">Our Services</h2>
  <div class="rule" style="left:572px;top:1482px;width:56px"></div>
  <div class="service" style="left:111px;top:1530px"><div class="photo s1" role="img" aria-label="Photo of colleagues reviewing data on a screen"></div><h3>LORUM IPSUM DOL</h3><p>Sed ut perspiciatis unde omnis iste natus err or sit voluptatem accusantium doloremque laudantium totam remea.</p></div>
  <div class="service" style="left:445px;top:1530px"><div class="photo s2" role="img" aria-label="Photo of a woman and man working at a desk"></div><h3>LORUM IPSUM DOL</h3><p>Sed ut perspiciatis unde omnis iste natus err or sit voluptatem accusantium doloremque laudantium totam remea.</p></div>
  <div class="service" style="left:779px;top:1530px"><div class="photo s3" role="img" aria-label="Photo of two colleagues looking at a laptop"></div><h3>LORUM IPSUM DOL</h3><p>Sed ut perspiciatis unde omnis iste natus err or sit voluptatem accusantium doloremque laudantium totam remea.</p></div>
  <div class="btn" style="left:189px;top:1940px;width:154px;height:49px">Learn More</div>
  <div class="btn" style="left:523px;top:1940px;width:154px;height:49px">Learn More</div>
  <div class="btn" style="left:857px;top:1940px;width:154px;height:49px">Learn More</div>

  <div class="why" role="img" aria-label="Purple tinted photo of a business team"></div>
  <h2 class="abs heading" style="left:0;width:1200px;text-align:center;top:2158px;font-size:38px;color:#fff">Why Choose Us</h2>
  <div class="abs" style="left:514px;top:2208px;width:172px;height:1px;background:rgba(255,255,255,.6)"></div>
  <div class="abs" style="left:572px;top:2207px;width:56px;height:3px;background:#fff"></div>

  <div class="card" style="left:111px;top:2258px">
    <svg width="40" height="48" viewBox="0 0 40 48"><circle cx="20" cy="18" r="15" fill="#fff"/><rect x="13" y="34" width="14" height="5" fill="#fff"/><rect x="15" y="41" width="10" height="4" fill="#fff"/></svg>
    <h4>Lorem ipsum dolor sit amet con sectetur adipiscing</h4>
    <p>Sed ut perspiciatis unde omnis iste natus error sit volupta tem accusantium doloremque laudantium, totam rem aperiam eaque ipsa quae ab illo.</p>
  </div>
  <div class="card white" style="left:612px;top:2258px">
    <svg width="50" height="50" viewBox="0 0 50 50"><circle cx="25" cy="25" r="21" fill="none" stroke="#5b2a7e" stroke-width="4"/><circle cx="25" cy="19" r="6" fill="#5b2a7e"/><path d="M13 36 Q25 22 37 36 Z" fill="#5b2a7e"/></svg>
    <h4>Lorem ipsum dolor sit amet con sectetur adipiscing</h4>
    <p>Sed ut perspiciatis unde omnis iste natus error sit volupta tem accusantium doloremque laudantium, totam rem aperiam eaque ipsa quae ab illo.</p>
  </div>
  <div class="card" style="left:111px;top:2479px">
    <svg width="56" height="56" viewBox="0 0 56 56" fill="none" stroke="#fff" stroke-width="3"><circle cx="28" cy="28" r="8"/><circle cx="9" cy="9" r="6"/><circle cx="47" cy="9" r="6"/><circle cx="9" cy="47" r="6"/><circle cx="47" cy="47" r="6"/><path d="M14 14 L22 22 M42 14 L34 22 M14 42 L22 34 M42 42 L34 34"/></svg>
    <h4>Lorem ipsum dolor sit amet con sectetur adipiscing</h4>
    <p>Sed ut perspiciatis unde omnis iste natus error sit volupta tem accusantium doloremque laudantium, totam rem aperiam eaque ipsa quae ab illo.</p>
  </div>
  <div class="card" style="left:612px;top:2479px">
    <svg width="54" height="54" viewBox="0 0 54 54"><circle cx="27" cy="27" r="24" fill="none" stroke="#fff" stroke-width="3"/><circle cx="27" cy="27" r="13" fill="none" stroke="#fff" stroke-width="7" stroke-dasharray="6 4"/><circle cx="27" cy="27" r="5" fill="#fff"/></svg>
    <h4>Lorem ipsum dolor sit amet con sectetur adipiscing</h4>
    <p>Sed ut perspiciatis unde omnis iste natus error sit volupta tem accusantium doloremque laudantium, totam rem aperiam eaque ipsa quae ab illo.</p>
  </div>

  <div class="ready-photo" role="img" aria-label="Photo of a man in glasses writing notes beside a laptop"></div>
  <div class="abs ready-ring">
    <h2 class="heading" style="font-size:27px;line-height:32px;color:#333">Get Ready To<br>Start?</h2>
    <div style="width:36px;height:3px;background:var(--purple);margin:14px auto 0"></div>
    <p style="font-size:13px;line-height:23px;color:#999;margin:16px 26px 0">Lorem ipsum dolor sit amet, consectetur adipisc ing elit, sed do eiusmod tem enim ad minim ven iam quis nostrud exercitea.</p>
    <div style="margin:16px auto 0;width:137px;height:46px;border-radius:24px;background:var(--purple);color:#fff;font-weight:700;font-size:15px;display:flex;align-items:center;justify-content:center">CONTACT US</div>
  </div>

  <h2 class="abs heading" style="left:0;width:1200px;text-align:center;top:3304px;font-size:38px">Success Stories</h2>
  <div class="rule-wide" style="left:514px;top:3355px;width:172px"></div>
  <div class="rule" style="left:572px;top:3354px;width:56px"></div>
  <div class="story" style="left:111px;top:3403px"><div class="photo p1" role="img" aria-label="Photo of a woman smiling at a laptop"></div><div class="caption"><p>Lorem ipsum dolor sit amet<br>consectetur adipiscing<br>elit sesumd do</p><a>READ MORE</a></div></div>
  <div class="story" style="left:445px;top:3403px"><div class="photo p2" role="img" aria-label="Photo of colleagues gathered around a laptop"></div><div class="caption"><p>Lorem ipsum dolor sit amet<br>consectetur adipiscing<br>elit sesumd do</p><a>READ MORE</a></div></div>
  <div class="story" style="left:779px;top:3403px"><div class="photo p3" role="img" aria-label="Photo of business partners meeting in an office"></div><div class="caption"><p>Lorem ipsum dolor sit amet<br>consectetur adipiscing<br>elit sesumd do</p><a>READ MORE</a></div></div>

  <footer class="footer">
    <div class="abs" style="left:114px;top:112px;display:flex;align-items:center;gap:12px">
      <div style="width:48px;height:48px;border-radius:50%;background:#fff"></div>
      <div style="font-family:'Montserrat',sans-serif;font-weight:700;font-size:19px;line-height:23px;text-transform:uppercase;letter-spacing:1px">Corvell<br>Acquisitions Group</div>
    </div>
    <h5 style="left:461px;top:55px">Navigation</h5>
    <ul style="left:461px;top:98px"><li>Home</li><li>About Us</li><li>Our Services</li><li>Why Choose Us</li><li>Events</li><li>Contact Us</li></ul>
    <h5 style="left:654px;top:55px">Other Links</h5>
    <ul style="left:654px;top:98px"><li>FAQs</li><li>Site Map</li><li>Privacy Policy</li><li>Terms Of Use</li></ul>
    <h5 style="left:844px;top:55px">Contact Info</h5>
    <div class="ci" style="top:92px"><div class="ring"><svg width="14" height="20" viewBox="0 0 14 20"><path d="M7 0a7 7 0 017 7c0 5-7 13-7 13S0 12 0 7a7 7 0 017-7z" fill="#5b2a7e"/><circle cx="7" cy="7" r="2.5" fill="#fff"/></svg></div><span>27 Harbour Row, Northgate,<br>United States</span></div>
    <div class="ci" style="top:155px"><div class="ring"><svg width="18" height="18" viewBox="0 0 24 24"><path fill="#5b2a7e" d="M6.6 10.8a15.1 15.1 0 006.6 6.6l2.2-2.2c.3-.3.7-.4 1-.2 1.1.4 2.3.6 3.6.6.6 0 1 .4 1 1V20c0 .6-.4 1-1 1C10.6 21 3 13.4 3 4c0-.6.4-1 1-1h3.5c.6 0 1 .4 1 1 0 1.3.2 2.5.6 3.6.1.3 0 .7-.2 1z"/></svg></div><span>+1 (555) 014 2290</span></div>
    <div class="ci" style="top:218px"><div class="ring"><svg width="18" height="14" viewBox="0 0 16 12"><rect width="16" height="12" rx="1" fill="#5b2a7e"/><path d="M0 1 L8 7 L16 1" stroke="#fff" stroke-width="1.5" fill="none"/></svg></div><span>hello@corvellgroup.example</span></div>
    <div class="abs" style="left:140px;top:311px;width:920px;height:1px;background:var(--footer-line)"></div>
    <p class="abs" style="left:0;width:1200px;top:326px;text-align:center;font-size:12px;color:#ddd">© 2022 Corvell Acquisitions Group &nbsp;|&nbsp; All Rights Reserved</p>
  </footer>
  <div class="social" aria-label="Social links"><i></i><i></i><i></i><i></i></div>

</div>
</body>
</html>
```